Business Card Design

I need a business card for a company based in London, UK. I provide garden design, landscaping and maintenance services. The company specialises in modern, urban gardens. It must be horizontal design, white paper and black simple (easy to read) font. The print must be on clear, white surrounding. I like design that use the colours black, yellow, grey and different shades of green. The design must be tidy. It must not be overloaded with decorating. Embodied a small picture of a fragment of garden or plant or leaf in the sun (it must be yellowish and greenish). It would be good if it's "live and energetic". I attached all text and logo that have to appear on the card.

Target Market(s)

architect, property designers, property management companies, large property owners

Industry/Entity Type

Landscaping

Contact Information for Business Card

All the text must be the same as on my old card which I attached.

Requirements
Must have
• modern, simple, tidy, professional look
green, yellow, black colours,
white surrounding,
simple readable black font on clear white surrounding,
a small picture of garden or plant or "sun lights through the tree canopy"
Nice to have
• graduate movement from light green to dark green
Should not have
• old style font,
text must no be placed on pictures or decorations,
red and blue colours,
picture on the reverse

```html
<!DOCTYPE html>
<html lang="en">
<head>
<meta charset="utf-8">
<title>Brightleaf Gardens – Business Card</title>
<link href="https://fonts.googleapis.com/css2?family=Open+Sans:wght@400;600;700&display=swap" rel="stylesheet">
<style>
  :root {
    --bg: #e6e7e9;
    --paper: #ffffff;
    --green-dark: #0f9447;
    --green-mid: #8cc63f;
    --green-light: #c3dc8f;
    --yellow: #f2e600;
    --ink: #3a3a3a;
    --ink-soft: #4d4d4d;
  }
  * { box-sizing: border-box; margin: 0; padding: 0; }
  html, body {
    width: 1200px; height: 800px; overflow: hidden;
    background: var(--bg);
    font-family: "Open Sans", Arial, sans-serif;
  }
  .stage { position: relative; width: 1200px; height: 800px; }
  .card {
    position: absolute; width: 540px; height: 309px;
    background: var(--paper);
    overflow: hidden;
  }
  /* ---------- Back: services ---------- */
  .card--back { left: 30px; top: 245px; }
  .side-bands { position: absolute; left: 0; top: 0; width: 20px; height: 260px; }
  .side-bands span { display: block; height: 25%; }
  .side-bands .b1 { background: var(--green-dark); }
  .side-bands .b2 { background: var(--green-mid); }
  .side-bands .b3 { background: var(--green-light); }
  .side-bands .b4 { background: var(--yellow); }
  .corner-tab {
    position: absolute; left: 0; top: 0; width: 40px; height: 14px;
    background: var(--green-dark);
  }
  .services { position: absolute; left: 40px; top: 30px; right: 20px; }
  .service { margin-bottom: 26px; }
  .service h3 {
    color: var(--green-dark); font-weight: 700; font-size: 16px;
    letter-spacing: 0.3px; line-height: 1.1;
  }
  .service p { color: var(--ink-soft); font-size: 10.5px; line-height: 1.5; }
  /* ---------- Front: contact ---------- */
  .card--front { left: 630px; top: 245px; }
  .offer { position: absolute; left: 0; top: 0; width: 165px; }
  .offer__tile {
    height: 74px; display: flex; flex-direction: column;
    align-items: center; justify-content: center; gap: 5px;
    color: #fff; font-size: 10px; font-weight: 600; letter-spacing: 0.6px;
  }
  .offer__tile--design { background: var(--green-dark); }
  .offer__tile--landscaping { background: var(--green-mid); }
  .offer__tile--maintenance { background: var(--green-light); }
  .offer__tile svg { width: 34px; height: 34px; }
  .brand {
    position: absolute; right: 28px; top: 98px;
    font-weight: 600; font-size: 26px; color: var(--ink);
    letter-spacing: 0.2px;
  }
  .person {
    position: absolute; right: 28px; top: 160px;
    color: var(--green-dark); font-weight: 700; font-size: 15px;
  }
  .address {
    position: absolute; right: 28px; top: 190px;
    color: var(--ink); font-weight: 700; font-size: 11.5px;
  }
  .contacts {
    position: absolute; left: 185px; right: 28px; top: 228px;
    display: flex; justify-content: space-between;
    font-size: 11.5px; color: var(--ink);
  }
  .contacts ul { list-style: none; }
  .contacts li { display: flex; align-items: center; gap: 6px; line-height: 1.7; }
  .contacts .phones li { justify-content: flex-end; }
  .icon { width: 11px; height: 11px; flex: none; }
</style>
</head>
<body>
<main class="stage">

  <section class="card card--back" aria-label="Business card reverse: services">
    <div class="corner-tab"></div>
    <div class="side-bands"><span class="b1"></span><span class="b2"></span><span class="b3"></span><span class="b4"></span></div>
    <div class="services">
      <article class="service"><h3>GARDEN DESIGN</h3><p>all styles: had-drawn &amp; CAD, detailed mapping, underground service tracing, soil analysis</p></article>
      <article class="service"><h3>GARDEN DESIGN</h3><p>all styles: had-drawn &amp; CAD, detailed mapping, underground service tracing, soil analysis</p></article>
      <article class="service"><h3>GARDEN DESIGN</h3><p>all styles: had-drawn &amp; CAD, detailed mapping, underground service tracing, soil analysis</p></article>
      <article class="service"><h3>GARDEN DESIGN</h3><p>all styles: had-drawn &amp; CAD, detailed mapping, underground service tracing, soil analysis</p></article>
    </div>
  </section>

  <section class="card card--front" aria-label="Business card front: contact details">
    <div class="offer">
      <div class="offer__tile offer__tile--design">
        <svg viewBox="0 0 34 34" aria-hidden="true"><circle cx="17" cy="17" r="15" fill="none" stroke="#fff" stroke-width="2"/><path d="M11 23 L12 19 L21 10 L24 13 L15 22 Z" fill="#fff"/></svg>
        DESIGN
      </div>
      <div class="offer__tile offer__tile--landscaping">
        <svg viewBox="0 0 34 34" aria-hidden="true"><circle cx="17" cy="17" r="15" fill="none" stroke="#fff" stroke-width="2"/><path d="M9 22 L14 14 L17 18 L20 13 L25 22 Z" fill="#fff"/></svg>
        LANDSCAPING
      </div>
      <div class="offer__tile offer__tile--maintenance">
        <svg viewBox="0 0 34 34" aria-hidden="true"><circle cx="17" cy="17" r="15" fill="none" stroke="#fff" stroke-width="2"/><path d="M11 11 L23 23 M23 11 L11 23" stroke="#fff" stroke-width="2.4" stroke-linecap="round"/></svg>
        MAINTENANCE
      </div>
    </div>

    <p class="brand">Brightleaf Gardens</p>

    <p class="person">Daniel Marsh</p>
    <p class="address">27 Mill Lane, Kingsford, KT9 4RB</p>

    <div class="contacts">
      <ul class="online">
        <li>info@brightleaf-gardens.co.uk
          <svg class="icon" viewBox="0 0 12 12" aria-hidden="true"><rect x="0.5" y="2" width="11" height="8" fill="var(--green-dark)"/><path d="M1 2.5 L6 6.5 L11 2.5" fill="none" stroke="#fff" stroke-width="1"/></svg></li>
        <li>www.brightleaf-gardens.co.uk
          <svg class="icon" viewBox="0 0 12 12" aria-hidden="true"><circle cx="6" cy="6" r="5.5" fill="var(--green-dark)"/><path d="M0.5 6 H11.5 M6 0.5 V11.5" stroke="#fff" stroke-width="0.8"/></svg></li>
      </ul>
      <ul class="phones">
        <li>02085550147
          <svg class="icon" viewBox="0 0 12 12" aria-hidden="true"><path d="M2 1 L4.5 1 L5 4 L3.5 5 C4.3 7 5 7.7 7 8.5 L8 7 L11 7.5 L11 10 C6 11 1 6 2 1 Z" fill="var(--green-dark)"/></svg></li>
        <li>07700900418
          <svg class="icon" viewBox="0 0 12 12" aria-hidden="true"><rect x="3" y="0.5" width="6" height="11" rx="1.2" fill="var(--green-dark)"/><rect x="4" y="2" width="4" height="6" fill="#fff"/></svg></li>
      </ul>
    </div>
  </section>

</main>
</body>
</html>
```